Slide Master for Halvern Engines - A Systematic Hedge Fund

We are looking for someone to produce a theme and slide master for us for our investor presentations. I have uploaded a few examples of templates that we would like to have included:
Main Title
Section Title
Slides with just bullet points
Different image/table configurations with bullet points and foot notes
Biographies of different lengths
A disclaimer (no one will read this but it should still look nice and needs to be in the presentations)
I have also uploaded the company logo, business card and colour definitions. Currently we have a blue colour scheme defined, but it would be nice to get a complementary set of colours so that when we have charts with more elements we can just draw from those.
The most important thing is that the slide master must be of general use to us. We arn't looking to have a specific presentation designed for us, but a theme/style that we can apply ourselves to any presentation we need to give in the future. It should have clearly defined guidelines for where content should go (and if this is different with and without footnotes for example). We would also like it to have a similar feel to the logo/business cards, so matt colours, high contrast, but not busy.
I'm excited to see the results!

```html
<!DOCTYPE html>
<html lang="en">
<head>
<meta charset="utf-8">
<title>Halvern Engines – Slide Master</title>
<link rel="stylesheet" href="https://fonts.googleapis.com/css2?family=Montserrat:wght@400;500;600;700;800&family=Arimo:wght@400;700&display=swap">
<style>
:root{
  --navy:#0f4470;
  --blue:#4a8fd0;
  --pale:#a8c6e8;
  --ink:#1c2430;
  --grey-bg:#808285;
  --white:#ffffff;
  --rule:#7a7f86;
  --ghost:#b8bfd2;
}
*{margin:0;padding:0;box-sizing:border-box}
html,body{width:1200px;height:857px;overflow:hidden}
body{background:var(--grey-bg);position:relative;font-family:"Montserrat",sans-serif;color:var(--ink)}
.slide{position:absolute;width:339px;height:190px;background:var(--white);overflow:hidden}
.slide.navy{background:var(--navy)}
.abs{position:absolute}

/* brand wordmark */
.brand{position:absolute;font-weight:800;color:var(--navy);text-transform:uppercase;text-align:center;line-height:1.05;letter-spacing:1px}
.brand-mark{display:block;margin:0 auto 4px;background:var(--navy)}
.brand.on-navy{color:var(--white)}
.brand.on-navy .brand-mark{background:var(--white)}
.brand.ghost{color:var(--ghost)}
.brand.ghost .brand-mark{background:var(--ghost)}
.brand-lg{font-size:17px;width:150px}
.brand-lg .brand-mark{width:14px;height:14px}
.brand-sm{font-size:7px;width:60px;letter-spacing:.5px}
.brand-sm .brand-mark{width:6px;height:6px;margin-bottom:2px}

.network{position:absolute;background:radial-gradient(ellipse at 70% 60%,rgba(74,143,208,.35),rgba(15,68,112,0) 65%)}

/* cover text */
.year{position:absolute;font-size:4.5px;font-weight:600}
.cover-title{position:absolute;font-size:16.5px;font-weight:700;line-height:1;letter-spacing:.8px}
.cover-sub{position:absolute;font-size:8px;font-weight:500;letter-spacing:.5px}
.btn{position:absolute;width:51px;height:12px;border:1px solid var(--navy);border-radius:7px;font-size:4.3px;font-weight:500;text-align:center;line-height:10px}
.btn.on-navy{border-color:var(--pale);color:var(--white)}

/* content slide header/footer */
.accent{position:absolute;left:3px;top:8px;width:2px;height:29px;background:var(--navy)}
.slide-title{position:absolute;left:10px;top:6px;font-size:16px;font-weight:700;color:var(--navy);letter-spacing:.4px}
.slide-sub{position:absolute;left:11px;top:26px;font-size:8.5px;font-weight:500;letter-spacing:.6px}
.slide .brand-sm{right:12px;top:7px}
.foot-text{position:absolute;left:11px;bottom:6px;font-size:2.6px}
.page-no{position:absolute;right:10px;bottom:6px;font-size:2.8px;font-weight:600}
.foot-line{position:absolute;left:0;right:0;bottom:0;height:2px;background:var(--blue)}

.col-head{position:absolute;font-size:5.2px;font-weight:700}
.col{position:absolute;font-size:2.55px;line-height:1.35;text-align:justify;color:#333}
.col p{margin-bottom:2.5px}

/* feature list */
.feature-icon{position:absolute;width:22px;height:22px;border-radius:50%}
.feature-head{position:absolute;font-size:5.5px;font-weight:700;color:var(--blue)}
.feature-text{position:absolute;font-size:2.55px;line-height:1.35;width:102px;text-align:justify}

.chart-title{position:absolute;font-family:"Arimo",sans-serif;font-size:4.3px;color:#555;text-align:center}

/* table */
.data-table{position:absolute;left:11px;top:51px;width:197px;border-collapse:collapse;font-family:"Arimo",sans-serif;font-size:2.7px}
.data-table th,.data-table td{border:.4px solid #777;padding:1.2px 1.5px;text-align:left;vertical-align:top}
.data-table th{font-weight:700;text-align:center}
.note-list{position:absolute;left:222px;top:50px;width:104px}
.note-list div{position:relative;font-size:2.5px;line-height:1.35;padding-left:5px;margin-bottom:8.5px}
.note-list div::before{content:"";position:absolute;left:0;top:0;width:.8px;height:100%;background:var(--navy)}

.check-row{position:absolute;left:13px;width:240px;font-size:2.5px;line-height:1.35;padding-left:9px}
.check-row svg{position:absolute;left:0;top:-.5px;width:6px;height:6px}

/* split agenda */
.panel{position:absolute;top:0;bottom:0;background:var(--navy)}
.agenda-head{position:absolute;font-size:7px;font-weight:700;color:var(--white)}
.agenda-head::before{content:"";position:absolute;left:-16px;top:1px;width:9px;height:7px;background:var(--pale)}
.agenda-item{position:absolute;font-size:5.8px;font-weight:600;color:var(--white)}
.agenda-item::before{content:"";position:absolute;left:-8px;top:2.5px;width:5px;height:2.4px;background:var(--pale)}

.body-text{position:absolute;font-size:2.55px;line-height:1.35;text-align:justify;color:var(--white)}
</style>
</head>
<body>

<!-- Row 1 -->
<section class="slide" style="left:74px;top:33px">
  <div class="brand brand-lg" style="left:95px;top:64px"><span class="brand-mark"></span>Halvern<br>Engines</div>
</section>

<section class="slide navy" style="left:425px;top:33px">
  <div class="network" role="img" aria-label="Faint connected-node network pattern" style="left:120px;top:0;width:219px;height:190px"></div>
  <div class="brand brand-lg on-navy" style="left:95px;top:64px"><span class="brand-mark"></span>Halvern<br>Engines</div>
</section>

<section class="slide" style="left:776px;top:33px">
  <div class="brand brand-lg" style="left:12px;top:64px"><span class="brand-mark"></span>Halvern<br>Engines</div>
  <div class="abs" style="left:172px;top:13px;width:.6px;height:166px;background:var(--rule)"></div>
  <div class="year" style="left:187px;top:27px">2021</div>
  <div class="cover-title" style="left:186px;top:35px;color:var(--navy)">Master Slide<br>Presentation</div>
  <div class="cover-sub" style="left:187px;top:72px">Subtitle Goes Here</div>
  <div class="btn" style="left:186px;top:151px">Learn More</div>
</section>

<!-- Row 2 -->
<section class="slide" style="left:74px;top:234px">
  <div class="panel" style="left:0;width:173px">
    <div class="network" role="img" aria-label="Faint connected-node network pattern" style="left:0;top:70px;width:173px;height:120px"></div>
  </div>
  <div class="year" style="left:13px;top:28px;color:var(--white)">2021</div>
  <div class="cover-title" style="left:13px;top:35px;color:var(--white)">Master Slide<br>Presentation</div>
  <div class="cover-sub" style="left:13px;top:73px;color:var(--blue)">Subtitle Goes Here</div>
  <div class="btn on-navy" style="left:13px;top:151px">Learn More</div>
  <div class="brand brand-lg" style="left:181px;top:64px"><span class="brand-mark"></span>Halvern<br>Engines</div>
</section>

<section class="slide" style="left:425px;top:236px">
  <div class="accent"></div>
  <div class="slide-title">Your Title Here</div>
  <div class="slide-sub">Subtitle Goes Here</div>
  <div class="brand brand-sm"><span class="brand-mark"></span>Halvern<br>Engines</div>
  <div class="col-head" style="left:13px;top:59px">Header Title</div>
  <div class="col-head" style="left:119px;top:58px">Header Title</div>
  <div class="col-head" style="left:225px;top:57px">Header Title</div>
  <div class="col" style="left:13px;top:68px;width:99px">
    <p>Our process applies systematic models to liquid markets, balancing risk across asset classes while keeping costs low and execution disciplined. Every position is sized by volatility and reviewed daily by the research team.</p>
    <p>Our process applies systematic models to liquid markets, balancing risk across asset classes while keeping costs low and execution disciplined. Every position is sized by volatility and reviewed daily by the research team.</p>
  </div>
  <div class="col" style="left:119px;top:68px;width:99px">
    <p>Our process applies systematic models to liquid markets, balancing risk across asset classes while keeping costs low and execution disciplined. Every position is sized by volatility and reviewed daily by the research team.</p>
    <p>Our process applies systematic models to liquid markets, balancing risk across asset classes while keeping costs low and execution disciplined. Every position is sized by volatility and reviewed daily by the research team.</p>
  </div>
  <div class="col" style="left:225px;top:67px;width:99px">
    <p>Our process applies systematic models to liquid markets, balancing risk across asset classes while keeping costs low and execution disciplined. Every position is sized by volatility and reviewed daily by the research team.</p>
    <p>Our process applies systematic models to liquid markets, balancing risk across asset classes while keeping costs low and execution disciplined. Every position is sized by volatility and reviewed daily by the research team.</p>
  </div>
  <div class="foot-text">Halvern Engines investor presentation, for professional investors only</div>
  <div class="page-no">PAGE NO 01</div>
  <div class="foot-line"></div>
</section>

<section class="slide" style="left:776px;top:236px">
  <div class="accent"></div>
  <div class="slide-title">Your Title Here</div>
  <div class="slide-sub">Subtitle Goes Here</div>
  <div class="brand brand-sm"><span class="brand-mark"></span>Halvern<br>Engines</div>
  <div class="col-head" style="left:13px;top:59px">Header Title</div>
  <div class="col-head" style="left:174px;top:59px">Header Title</div>
  <div class="col" style="left:13px;top:68px;width:152px">
    <p>Our process applies systematic models to liquid markets, balancing risk across asset classes while keeping costs low and execution disciplined. Every position is sized by volatility and reviewed daily by the research team.</p>
    <p>Our process applies systematic models to liquid markets, balancing risk across asset classes while keeping costs low and execution disciplined. Every position is sized by volatility and reviewed daily by the research team.</p>
    <p>Our process applies systematic models to liquid markets, balancing risk across asset classes while keeping costs low and execution disciplined. Every position is sized by volatility and reviewed daily by the research team.</p>
  </div>
  <div class="col" style="left:174px;top:68px;width:152px">
    <p>Our process applies systematic models to liquid markets, balancing risk across asset classes while keeping costs low and execution disciplined. Every position is sized by volatility and reviewed daily by the research team.</p>
    <p>Our process applies systematic models to liquid markets, balancing risk across asset classes while keeping costs low and execution disciplined. Every position is sized by volatility and reviewed daily by the research team.</p>
    <p>Our process applies systematic models to liquid markets, balancing risk across asset classes while keeping costs low and execution disciplined. Every position is sized by volatility and reviewed daily by the research team.</p>
  </div>
  <div class="foot-text">Halvern Engines investor presentation, for professional investors only</div>
  <div class="page-no">PAGE NO 01</div>
  <div class="foot-line"></div>
</section>

<!-- Row 3 -->
<section class="slide" style="left:73px;top:440px">
  <div class="accent"></div>
  <div class="slide-title">Your Title Here</div>
  <div class="slide-sub">Subtitle Goes Here</div>
  <div class="brand brand-sm"><span class="brand-mark"></span>Halvern<br>Engines</div>

  <div class="feature-icon" style="left:13px;top:58px;background:var(--blue)">
    <svg viewBox="0 0 22 22" width="22" height="22"><g fill="none" stroke="#fff" stroke-width="1.2"><circle cx="11" cy="8.5" r="2.3"/><path d="M6.8 16c0-2.6 1.9-4.2 4.2-4.2s4.2 1.6 4.2 4.2"/><circle cx="6.5" cy="9.5" r="1.7"/><circle cx="15.5" cy="9.5" r="1.7"/></g></svg>
  </div>
  <div class="feature-head" style="left:44px;top:59px">Header Title</div>
  <div class="feature-text" style="left:44px;top:67px">Systematic models size each position by volatility and review risk daily.</div>

  <div class="feature-icon" style="left:13px;top:91px;background:var(--pale)">
    <svg viewBox="0 0 22 22" width="22" height="22"><g fill="none" stroke="#fff" stroke-width="1.2"><circle cx="11" cy="8.5" r="2.3"/><path d="M6.8 16c0-2.6 1.9-4.2 4.2-4.2s4.2 1.6 4.2 4.2"/><circle cx="6.5" cy="9.5" r="1.7"/><circle cx="15.5" cy="9.5" r="1.7"/></g></svg>
  </div>
  <div class="feature-head" style="left:44px;top:92px">Header Title</div>
  <div class="feature-text" style="left:44px;top:100px">Systematic models size each position by volatility and review risk daily.</div>

  <div class="feature-icon" style="left:13px;top:124px;background:var(--navy)">
    <svg viewBox="0 0 22 22" width="22" height="22"><g fill="none" stroke="#fff" stroke-width="1.2"><circle cx="11" cy="8.5" r="2.3"/><path d="M6.8 16c0-2.6 1.9-4.2 4.2-4.2s4.2 1.6 4.2 4.2"/><circle cx="6.5" cy="9.5" r="1.7"/><circle cx="15.5" cy="9.5" r="1.7"/></g></svg>
  </div>
  <div class="feature-head" style="left:44px;top:124px">Header Title</div>
  <div class="feature-text" style="left:44px;top:132px">Systematic models size each position by volatility and review risk daily.</div>

  <div class="chart-title" style="left:166px;top:55px;width:164px">Title of Barchart</div>
  <svg class="abs" style="left:160px;top:60px" width="176" height="98" viewBox="0 0 300 167">
    <g font-family="Arimo,sans-serif" font-size="6" fill="#555" text-anchor="end">
      <text x="26" y="12">800</text><text x="26" y="27">700</text><text x="26" y="42">600</text><text x="26" y="57">500</text><text x="26" y="72">400</text><text x="26" y="87">300</text><text x="26" y="102">200</text><text x="26" y="117">100</text><text x="26" y="132">0</text>
    </g>
    <g stroke="#ddd" stroke-width=".5"><line x1="30" y1="10" x2="290" y2="10"/><line x1="30" y1="25" x2="290" y2="25"/><line x1="30" y1="40" x2="290" y2="40"/><line x1="30" y1="55" x2="290" y2="55"/><line x1="30" y1="70" x2="290" y2="70"/><line x1="30" y1="85" x2="290" y2="85"/><line x1="30" y1="100" x2="290" y2="100"/><line x1="30" y1="115" x2="290" y2="115"/></g>
    <g fill="#0f4470" stroke="#fff" stroke-width=".4">
      <rect x="30" y="124" width="17.3" height="6"/><rect x="47.3" y="115" width="17.3" height="15"/><rect x="64.7" y="121" width="17.3" height="9"/><rect x="82" y="94" width="17.3" height="36"/><rect x="99.3" y="62.5" width="17.3" height="67.5"/><rect x="116.7" y="34" width="17.3" height="96"/><rect x="134" y="22" width="17.3" height="108"/><rect x="151.3" y="52" width="17.3" height="78"/><rect x="168.7" y="58" width="17.3" height="72"/><rect x="186" y="62.5" width="17.3" height="67.5"/><rect x="203.3" y="97" width="17.3" height="33"/><rect x="220.7" y="95.5" width="17.3" height="34.5"/><rect x="238" y="103" width="17.3" height="27"/><rect x="255.3" y="124" width="17.3" height="6"/><rect x="272.7" y="113.5" width="17.3" height="16.5"/>
    </g>
    <line x1="30" y1="130" x2="290" y2="130" stroke="#555" stroke-width=".6"/>
    <g font-family="Arimo,sans-serif" font-size="5.5" fill="#555" text-anchor="end">
      <text transform="translate(40 137) rotate(-35)">[151,161]</text><text transform="translate(57 137) rotate(-35)">(161,171]</text><text transform="translate(75 137) rotate(-35)">(171,181]</text><text transform="translate(92 137) rotate(-35)">(181,191]</text><text transform="translate(109 137) rotate(-35)">(191,201]</text><text transform="translate(127 137) rotate(-35)">(201,211]</text><text transform="translate(144 137) rotate(-35)">(211,221]</text><text transform="translate(161 137) rotate(-35)">(221,231]</text><text transform="translate(179 137) rotate(-35)">(231,241]</text><text transform="translate(196 137) rotate(-35)">(241,251]</text><text transform="translate(213 137) rotate(-35)">(251,261]</text><text transform="translate(231 137) rotate(-35)">(261,271]</text><text transform="translate(248 137) rotate(-35)">(271,281]</text><text transform="translate(265 137) rotate(-35)">(281,291]</text><text transform="translate(283 137) rotate(-35)">(291,301]</text>
    </g>
  </svg>
  <div class="foot-text">Halvern Engines investor presentation, for professional investors only</div>
  <div class="page-no">PAGE NO 01</div>
  <div class="foot-line"></div>
</section>

<section class="slide" style="left:423px;top:440px">
  <div class="accent"></div>
  <div class="slide-title">Your Title Here</div>
  <div class="slide-sub">Subtitle Goes Here</div>
  <div class="brand brand-sm"><span class="brand-mark"></span>Halvern<br>Engines</div>
  <table class="data-table">
    <tr><th>purchase<br>_time</th><th>sales<br>_id</th><th>customer<br>_id</th><th>currency</th><th>amount<br>_paid</th><th>device</th><th>has<br>_discount</th><th>agent_comment</th></tr>
    <tr><td>2018-01-01 8:48:00</td><td>466</td><td>1234</td><td>USD</td><td>$98.23</td><td>mobile app</td><td>FALSE</td><td></td></tr>
    <tr><td>2018-01-01 9:15:00</td><td>467</td><td>3485</td><td>USD</td><td>$34.35</td><td>desktop</td><td>TRUE</td><td>out of stock in blue - accepted switch to green for a 5% discount</td></tr>
    <tr><td>2018-01-01 15:12:00</td><td>468</td><td>875</td><td>USD</td><td>$34.35</td><td>mobile web</td><td>FALSE</td><td></td></tr>
    <tr><td>2018-01-01 16:48:00</td><td>469</td><td>875</td><td>USD</td><td>$34.35</td><td>desktop</td><td>FALSE</td><td></td></tr>
    <tr><td>2018-01-01 18:09:00</td><td>470</td><td>5246</td><td>USD</td><td>$34.35</td><td>mobile web</td><td>FALSE</td><td></td></tr>
    <tr><td>2018-01-01 18:33:00</td><td>471</td><td>9872</td><td>USD</td><td>$34.35</td><td>mobile web</td><td>FALSE</td><td></td></tr>
    <tr><td>2018-01-02 7:25:00</td><td>472</td><td>2498</td><td>USD</td><td>$34.35</td><td>desktop</td><td>FALSE</td><td></td></tr>
    <tr><td>2018-01-02 8:01:00</td><td>473</td><td>7892</td><td>USD</td><td>$34.35</td><td>desktop</td><td>FALSE</td><td></td></tr>
  </table>
  <div class="col" style="left:11px;top:151px;width:197px;font-weight:700">Our process applies systematic models to liquid markets, balancing risk across asset classes while keeping costs low and execution disciplined. Every position is sized by volatility and reviewed daily by the research team.</div>
  <div class="note-list">
    <div>Systematic models size each position by volatility and review risk daily.</div>
    <div>Systematic models size each position by volatility and review risk daily.</div>
    <div>Systematic models size each position by volatility and review risk daily.</div>
    <div>Systematic models size each position by volatility and review risk daily.</div>
    <div>Systematic models size each position by volatility and review risk daily.</div>
  </div>
  <div class="foot-text">Halvern Engines investor presentation, for professional investors only</div>
  <div class="page-no">PAGE NO 01</div>
  <div class="foot-line"></div>
</section>

<section class="slide" style="left:776px;top:440px">
  <div class="accent"></div>
  <div class="slide-title">Your Title Here</div>
  <div class="slide-sub">Subtitle Goes Here</div>
  <div class="brand brand-sm"><span class="brand-mark"></span>Halvern<br>Engines</div>
  <div class="check-row" style="top:48px"><svg viewBox="0 0 6 6"><circle cx="3" cy="3" r="3" fill="#4a8fd0"/><path d="M1.6 3.1l1 1 1.8-2" fill="none" stroke="#fff" stroke-width=".6"/></svg>Systematic models size each position by volatility and review risk daily. Systematic models size each position by volatility and review risk daily.</div>
  <div class="check-row" style="top:58px"><svg viewBox="0 0 6 6"><circle cx="3" cy="3" r="3" fill="#4a8fd0"/><path d="M1.6 3.1l1 1 1.8-2" fill="none" stroke="#fff" stroke-width=".6"/></svg>Systematic models size each position by volatility and review risk daily. Systematic models size each position by volatility and review risk daily.</div>
  <div class="check-row" style="top:68px"><svg viewBox="0 0 6 6"><circle cx="3" cy="3" r="3" fill="#4a8fd0"/><path d="M1.6 3.1l1 1 1.8-2" fill="none" stroke="#fff" stroke-width=".6"/></svg>Systematic models size each position by volatility and review risk daily. Systematic models size each position by volatility and review risk daily.</div>

  <div class="chart-title" style="left:20px;top:85px;width:144px">Title of Barchart</div>
  <svg class="abs" style="left:12px;top:90px" width="155" height="87" viewBox="0 0 300 167">
    <g font-family="Arimo,sans-serif" font-size="6" fill="#555" text-anchor="end">
      <text x="26" y="12">800</text><text x="26" y="27">700</text><text x="26" y="42">600</text><text x="26" y="57">500</text><text x="26" y="72">400</text><text x="26" y="87">300</text><text x="26" y="102">200</text><text x="26" y="117">100</text><text x="26" y="132">0</text>
    </g>
    <g stroke="#ddd" stroke-width=".5"><line x1="30" y1="10" x2="290" y2="10"/><line x1="30" y1="25" x2="290" y2="25"/><line x1="30" y1="40" x2="290" y2="40"/><line x1="30" y1="55" x2="290" y2="55"/><line x1="30" y1="70" x2="290" y2="70"/><line x1="30" y1="85" x2="290" y2="85"/><line x1="30" y1="100" x2="290" y2="100"/><line x1="30" y1="115" x2="290" y2="115"/></g>
    <g fill="#0f4470" stroke="#fff" stroke-width=".4">
      <rect x="30" y="124" width="17.3" height="6"/><rect x="47.3" y="115" width="17.3" height="15"/><rect x="64.7" y="121" width="17.3" height="9"/><rect x="82" y="94" width="17.3" height="36"/><rect x="99.3" y="62.5" width="17.3" height="67.5"/><rect x="116.7" y="34" width="17.3" height="96"/><rect x="134" y="22" width="17.3" height="108"/><rect x="151.3" y="52" width="17.3" height="78"/><rect x="168.7" y="58" width="17.3" height="72"/><rect x="186" y="62.5" width="17.3" height="67.5"/><rect x="203.3" y="97" width="17.3" height="33"/><rect x="220.7" y="95.5" width="17.3" height="34.5"/><rect x="238" y="103" width="17.3" height="27"/><rect x="255.3" y="124" width="17.3" height="6"/><rect x="272.7" y="113.5" width="17.3" height="16.5"/>
    </g>
    <line x1="30" y1="130" x2="290" y2="130" stroke="#555" stroke-width=".6"/>
    <g font-family="Arimo,sans-serif" font-size="5.5" fill="#555" text-anchor="end">
      <text transform="translate(40 137) rotate(-35)">[151,161]</text><text transform="translate(57 137) rotate(-35)">(161,171]</text><text transform="translate(75 137) rotate(-35)">(171,181]</text><text transform="translate(92 137) rotate(-35)">(181,191]</text><text transform="translate(109 137) rotate(-35)">(191,201]</text><text transform="translate(127 137) rotate(-35)">(201,211]</text><text transform="translate(144 137) rotate(-35)">(211,221]</text><text transform="translate(161 137) rotate(-35)">(221,231]</text><text transform="translate(179 137) rotate(-35)">(231,241]</text><text transform="translate(196 137) rotate(-35)">(241,251]</text><text transform="translate(213 137) rotate(-35)">(251,261]</text><text transform="translate(231 137) rotate(-35)">(261,271]</text><text transform="translate(248 137) rotate(-35)">(271,281]</text><text transform="translate(265 137) rotate(-35)">(281,291]</text><text transform="translate(283 137) rotate(-35)">(291,301]</text>
    </g>
  </svg>

  <div class="chart-title" style="left:172px;top:84px;width:144px">Title of Barchart</div>
  <svg class="abs" style="left:164px;top:89px" width="155" height="87" viewBox="0 0 300 167">
    <g font-family="Arimo,sans-serif" font-size="6" fill="#555" text-anchor="end">
      <text x="26" y="12">800</text><text x="26" y="27">700</text><text x="26" y="42">600</text><text x="26" y="57">500</text><text x="26" y="72">400</text><text x="26" y="87">300</text><text x="26" y="102">200</text><text x="26" y="117">100</text><text x="26" y="132">0</text>
    </g>
    <g stroke="#ddd" stroke-width=".5"><line x1="30" y1="10" x2="290" y2="10"/><line x1="30" y1="25" x2="290" y2="25"/><line x1="30" y1="40" x2="290" y2="40"/><line x1="30" y1="55" x2="290" y2="55"/><line x1="30" y1="70" x2="290" y2="70"/><line x1="30" y1="85" x2="290" y2="85"/><line x1="30" y1="100" x2="290" y2="100"/><line x1="30" y1="115" x2="290" y2="115"/></g>
    <g fill="#0f4470" stroke="#fff" stroke-width=".4">
      <rect x="30" y="124" width="17.3" height="6"/><rect x="47.3" y="115" width="17.3" height="15"/><rect x="64.7" y="121" width="17.3" height="9"/><rect x="82" y="94" width="17.3" height="36"/><rect x="99.3" y="62.5" width="17.3" height="67.5"/><rect x="116.7" y="34" width="17.3" height="96"/><rect x="134" y="22" width="17.3" height="108"/><rect x="151.3" y="52" width="17.3" height="78"/><rect x="168.7" y="58" width="17.3" height="72"/><rect x="186" y="62.5" width="17.3" height="67.5"/><rect x="203.3" y="97" width="17.3" height="33"/><rect x="220.7" y="95.5" width="17.3" height="34.5"/><rect x="238" y="103" width="17.3" height="27"/><rect x="255.3" y="124" width="17.3" height="6"/><rect x="272.7" y="113.5" width="17.3" height="16.5"/>
    </g>
    <line x1="30" y1="130" x2="290" y2="130" stroke="#555" stroke-width=".6"/>
    <g font-family="Arimo,sans-serif" font-size="5.5" fill="#555" text-anchor="end">
      <text transform="translate(40 137) rotate(-35)">[151,161]</text><text transform="translate(57 137) rotate(-35)">(161,171]</text><text transform="translate(75 137) rotate(-35)">(171,181]</text><text transform="translate(92 137) rotate(-35)">(181,191]</text><text transform="translate(109 137) rotate(-35)">(191,201]</text><text transform="translate(127 137) rotate(-35)">(201,211]</text><text transform="translate(144 137) rotate(-35)">(211,221]</text><text transform="translate(161 137) rotate(-35)">(221,231]</text><text transform="translate(179 137) rotate(-35)">(231,241]</text><text transform="translate(196 137) rotate(-35)">(241,251]</text><text transform="translate(213 137) rotate(-35)">(251,261]</text><text transform="translate(231 137) rotate(-35)">(261,271]</text><text transform="translate(248 137) rotate(-35)">(271,281]</text><text transform="translate(265 137) rotate(-35)">(281,291]</text><text transform="translate(283 137) rotate(-35)">(291,301]</text>
    </g>
  </svg>
  <div class="foot-text">Halvern Engines investor presentation, for professional investors only</div>
  <div class="page-no">PAGE NO 01</div>
  <div class="foot-line"></div>
</section>

<!-- Row 4 -->
<section class="slide" style="left:74px;top:640px">
  <div class="brand brand-lg" style="left:8px;top:66px"><span class="brand-mark"></span>Halvern<br>Engines</div>
  <div class="panel" style="left:169px;width:170px"></div>
  <div class="abs" style="left:168px;top:17px;width:2px;height:29px;background:var(--blue)"></div>
  <div class="abs" style="left:177px;top:15px;font-size:16px;font-weight:700;color:var(--white);letter-spacing:.4px">Your Title Here</div>
  <div class="abs" style="left:178px;top:35px;font-size:8.5px;font-weight:500;color:var(--blue);letter-spacing:.6px">Subtitle Goes Here</div>
  <div class="agenda-head" style="left:179px;top:73px">Header Title</div>
  <div class="agenda-item" style="left:189px;top:84px">Text Goes Here</div>
  <div class="agenda-item" style="left:189px;top:93px">Text Goes Here</div>
  <div class="agenda-item" style="left:189px;top:102px">Text Goes Here</div>
  <div class="agenda-item" style="left:189px;top:111px">Text Goes Here</div>
  <div class="agenda-head" style="left:179px;top:138px">Header Title</div>
  <div class="agenda-item" style="left:189px;top:149px">Text Goes Here</div>
  <div class="agenda-item" style="left:189px;top:158px">Text Goes Here</div>
</section>

<section class="slide" style="left:425px;top:640px">
  <div class="brand brand-lg ghost" style="left:22px;top:66px"><span class="brand-mark"></span>Halvern<br>Engines</div>
  <div class="panel" style="left:197px;width:142px"></div>
  <div class="brand brand-sm on-navy" style="left:218px;top:22px;width:80px;font-size:10px"><span class="brand-mark" style="width:8px;height:8px"></span>Halvern<br>Engines</div>
  <div class="abs" style="left:223px;top:67px;width:.6px;height:63px;background:var(--white)"></div>
  <div class="abs" style="left:223px;top:133px;font-size:10.5px;font-weight:700;color:var(--white)">Section Title</div>
  <div class="abs" style="left:223px;top:145px;font-size:5.5px;font-weight:500;color:var(--blue);letter-spacing:.3px">Subtitle Goes Here</div>
  <div class="body-text" style="left:223px;top:153px;width:100px">Our process applies systematic models to liquid markets, balancing risk across asset classes while keeping costs low and execution disciplined. Every position is sized by volatility and reviewed daily by the research team.</div>
</section>

<section class="slide" style="left:775px;top:641px">
  <div class="brand brand-sm" style="left:125px;top:10px;width:90px;font-size:10px;right:auto"><span class="brand-mark" style="width:8px;height:8px"></span>Halvern<br>Engines</div>
  <div class="panel" style="left:0;right:0;top:51px"></div>
  <div class="abs" style="left:0;right:0;top:50px;height:1.5px;background:var(--blue)"></div>
  <div class="abs" style="left:0;right:0;top:69px;text-align:center;font-size:16px;font-weight:700;color:var(--white);letter-spacing:.4px">Your Title Here</div>
  <div class="abs" style="left:0;right:0;top:89px;text-align:center;font-size:5.5px;font-weight:500;color:var(--blue);letter-spacing:.3px">Subtitle Goes Here</div>
  <div class="abs" style="left:145px;top:97px;width:49px;height:.5px;background:var(--pale)"></div>
  <div class="body-text" style="left:16px;top:108px;width:307px">Our process applies systematic models to liquid markets, balancing risk across asset classes while keeping costs low and execution disciplined. Every position is sized by volatility and reviewed daily by the research team. Our process applies systematic models to liquid markets, balancing risk across asset classes while keeping costs low and execution disciplined. Every position is sized by volatility and reviewed daily by the research team. Our process applies systematic models to liquid markets, balancing risk across asset classes while keeping costs low and execution disciplined. Every position is sized by volatility and reviewed daily by the research team.</div>
  <div class="body-text" style="left:16px;top:148px;width:307px">Our process applies systematic models to liquid markets, balancing risk across asset classes while keeping costs low and execution disciplined. Every position is sized by volatility and reviewed daily by the research team.</div>
</section>

</body>
</html>
```